Residential Construction Business - Site Signage

I need a design made for a site fence banner. We have a logo and branding so the design would need to be aligned with this. It would need to be made to specific size ratio so that it can be sent to the maker for production.
ratio : 4600 wide x 1700 high
The design should feature our website and also the slogan
"Stay home, build anew"

Target Market(s)

potential clients

Industry/Entity Type

construction

Font styles to use
Other font styles liked:
• to match branding

Colors
0054AA
0677BA
7BADD7
CADEEF
E8F1F8

Requirements
Must have
• www.velmbuild.com.au Majority of the sign is our brand logo
Nice to have
• Majority of the sign is our brand logo
Should not have
• colors and themes that arent brand relevant

```html
<!DOCTYPE html>
<html lang="en">
<head>
<meta charset="utf-8">
<title>Velm Build – Site Fence Banner</title>
<link rel="stylesheet" href="https://fonts.googleapis.com/css2?family=Montserrat:wght@500;600&display=swap">
<style>
  :root {
    --backdrop: #c0c0c0;
    --paper: #ffffff;
    --navy: #053c5e;
    --ink-light: #ffffff;
  }
  html, body {
    margin: 0;
    padding: 0;
    width: 1200px;
    height: 1200px;
    overflow: hidden;
    background: var(--backdrop);
  }
  .banner {
    position: absolute;
    left: 94px;
    top: 412px;
    width: 1015px;
    height: 379px;
    background: var(--paper);
    box-shadow: 0 0 18px rgba(0, 0, 0, 0.45);
    font-family: "Montserrat", Arial, sans-serif;
    overflow: hidden;
  }
  .banner__shape {
    position: absolute;
    inset: 0;
    width: 100%;
    height: 100%;
  }
  .banner__shape path { fill: var(--navy); }
  .brand-name {
    position: absolute;
    left: 256px;
    top: 162px;
    margin: 0;
    font-size: 54px;
    font-weight: 500;
    letter-spacing: 0.33em;
    line-height: 1;
    color: var(--ink-light);
    white-space: nowrap;
  }
  .divider {
    position: absolute;
    left: 747px;
    top: 147px;
    width: 1.5px;
    height: 101px;
    background: var(--ink-light);
  }
  .tagline {
    position: absolute;
    left: 772px;
    top: 160px;
    margin: 0;
    font-size: 24px;
    font-weight: 500;
    letter-spacing: 0.22em;
    line-height: 45px;
    color: var(--ink-light);
    white-space: nowrap;
  }
  .website {
    position: absolute;
    left: 772px;
    top: 306px;
    margin: 0;
    font-size: 16.5px;
    font-weight: 500;
    letter-spacing: 0.02em;
    color: var(--ink-light);
    white-space: nowrap;
  }
</style>
</head>
<body>
  <section class="banner">
    <svg class="banner__shape" viewBox="0 0 1015 379" preserveAspectRatio="none" aria-hidden="true">
      <path d="M399 0 H1015 V379 H413 L252 217 Q229 188 251 161 Z"/>
    </svg>
    <h1 class="brand-name">VELMBUILD</h1>
    <div class="divider"></div>
    <p class="tagline">STAY HOME,<br>BUILD ANEW</p>
    <p class="website">www.velmbuild.com.au</p>
  </section>
</body>
</html>
```